Podcast covert art for startup show

I need podcast cover art that stands out and clearly says what the podcast is about: startup stories.

This is an example of Castrova cover art:
https://www.filebarnex.com/s/q4k8tmwpl2vbx9r/Castrova%202.png?dl=0

You can see how mine is looking blah on this page:
https://www.filebarnex.com/s/7h3jrdkqa5wzm2f/My%20podcast%20art%20doesn%27t%20stand%20out%20enough.png?dl=0

I need something that will get attention on a page that's full of other podcast covers and be easy to read.

SOMETHINGS THAT MIGHT HELP:

I love how easy it is to read the titles of these podcasts:
https://www.filebarnex.com/s/wpx6ghtmr0cqv84/easy%20to%20read%20titles.png?dl=0

I love how the logos of these podcasts are easy to read but they don't take much space:
https://www.filebarnex.com/s/5t2yfnbkd8jxe63/nice%20logo%20placement.png?dl=0

Target Market(s)

Successful software entrepreneurs

Industry/Entity Type

Startup

Font styles to use
Serif

Colors
00a990

Requirements
Must have
• I need it to include this:
• - This phrase: Startup Stories
• - My logo (keep it small, but readable)
• - My photo
• MY LOGO:
• http://talvoren.com/logo
• MY FAVORITE PHOTO OF MYSELF:
• https://vault.stormlake.net/open?id=0Xq7T_pwkr5bnHYmQZAaLPKKRw3
• You can edit my photo any way you want, including removing the background, turning me into a black&white photo, etc
• OTHER PHOTOS OF ME:
• https://vault.stormlake.net/open?id=0Xq7T_pwkr5bnW8JdvqXAcMbPZN
• Castrova asks that the size be 3000 x 3000 pixels
Nice to have
• I prefer that it have have 1 dominating color to help it stand out.
• This is what I mean:
• https://www.filebarnex.com/s/q4k8tmwpl2vbx9r/Castrova%20-%20one%20dominating%20color.png?dl=0
• I really like this color:
• https://www.filebarnex.com/s/k9v1wfzhr3ndy7c/color%20I%20like.png?dl=0

```html
<!DOCTYPE html>
<html lang="en">
<head>
<meta charset="utf-8">
<title>Startup Stories – Podcast Cover</title>
<link rel="stylesheet" href="https://fonts.googleapis.com/css2?family=Bebas+Neue&family=Barlow:wght@600&display=swap">
<style>
  :root {
    --teal-base: #01a78f;
    --teal-mid: #05b9a3;
    --teal-light: #0bd3c3;
    --logo-plate: #221e2b;
    --ink-white: #ffffff;
    --photo-warm: #c8281c;
    --photo-deep: #3a2320;
  }
  html, body {
    margin: 0;
    padding: 0;
    width: 1200px;
    height: 1200px;
    overflow: hidden;
    background: var(--teal-base);
  }
  .cover {
    position: relative;
    width: 1200px;
    height: 1200px;
    overflow: hidden;
  }
  .cover-backdrop {
    position: absolute;
    inset: 0;
  }
  .brand-plate {
    position: absolute;
    left: 62px;
    top: 68px;
    width: 450px;
    height: 133px;
    background: var(--logo-plate);
    display: flex;
    align-items: center;
    justify-content: center;
  }
  .brand-name {
    font-family: "Barlow", "Arial Narrow", sans-serif;
    font-weight: 600;
    font-size: 78px;
    letter-spacing: 6px;
    color: var(--ink-white);
    line-height: 1;
  }
  .host-photo {
    position: absolute;
    left: 808px;
    top: 41px;
    width: 324px;
    height: 324px;
    border-radius: 50%;
    background: radial-gradient(circle at 50% 55%, var(--photo-deep) 0%, #6b2a20 45%, var(--photo-warm) 80%);
  }
  .show-title {
    position: absolute;
    inset: 0;
  }
  .show-title text {
    font-family: "Bebas Neue", "Oswald", sans-serif;
    font-size: 333px;
    fill: var(--ink-white);
  }
</style>
</head>
<body>
  <main class="cover">
    <svg class="cover-backdrop" width="1200" height="1200" viewBox="0 0 1200 1200" aria-hidden="true">
      <rect width="1200" height="1200" fill="var(--teal-base)"/>
      <polygon points="278,1200 1118,0 1200,0 1200,1200" fill="var(--teal-mid)"/>
      <polygon points="548,0 1200,0 1200,933" fill="var(--teal-light)" opacity="0.85"/>
    </svg>

    <div class="brand-plate">
      <span class="brand-name">TALVOREN</span>
    </div>

    <div class="host-photo" role="img" aria-label="Portrait of the show host, smiling with a fist raised, against a red painted background"></div>

    <svg class="show-title" width="1200" height="1200" viewBox="0 0 1200 1200">
      <title>Startup Stories</title>
      <text x="323" y="866" textLength="795" lengthAdjust="spacingAndGlyphs">STARTUP</text>
      <text x="323" y="1128" textLength="795" lengthAdjust="spacingAndGlyphs">STORIES</text>
    </svg>
  </main>
</body>
</html>
```